Business Card Professional Clean - Lumavault

Create a business card for my company that deals with Cryptocurrencies. I have a few designs ideas that I'd like to be implemented. Thanks! I will include the logo files, and a link to the design styles that I like.

Target Market(s)

Professionals

Industry/Entity Type

Consulting

Contact Information for Business Card

Name: Mark Dunn
Title: CEO/Technical Director
Phone: (587)943-0586
E-mail: mdunn@lumavault.ca
Address: Suite 512, 208-3370 Harwood Avenue NW

Twitter: @LumaVaultHQ
Instagram: lumavaulthq

Colors
92b5d7
3276b5
33a6d7
85acd3
85cae6
0592cd

Requirements
Must have
• Some colors that match with the logo and the pictures I put in below.
• Ideally the finished product would look something like the attachments showing the color gradient I want.
Nice to have
• Please see some of the attachments I've included. This is very close to the final product that I would like to see. If someone could recreate something like those I would definitely feel pretty good about it.
• For the instagram and twitter please use the symbols/icon to represent it on the card.
Should not have
• No crazy colors and unprofessional styles. I just want clear info. Don't go outside the boundaries of the colors in the attachment and we should be good. No crazy weird fonts either.

```html
<!DOCTYPE html>
<html lang="en">
<head>
<meta charset="utf-8">
<title>Lumavault – Business Card</title>
<link rel="stylesheet" href="https://fonts.googleapis.com/css2?family=Raleway:wght@300;400;500;600&display=swap">
<style>
  :root {
    --page: #e6e7e9;
    --navy: #3a4759;
    --navy-tab: #44546a;
    --blue: #1f8fd1;
    --grey: #d6d7d9;
    --white: #ffffff;
    --ink: #2f3846;
    --ink-soft: #55606e;
    --accent: #3276b5;
    --on-navy: #e9edf2;
  }
  * { box-sizing: border-box; margin: 0; padding: 0; }
  html, body {
    width: 1200px; height: 873px; overflow: hidden;
    background: var(--page);
    font-family: "Raleway", Arial, sans-serif;
  }
  .stage {
    position: relative; width: 1200px; height: 873px;
    display: flex; align-items: center; justify-content: center; gap: 60px;
  }
  .card {
    position: relative; width: 520px; height: 297px; overflow: hidden;
    box-shadow: 0 10px 28px rgba(30, 40, 55, .18);
  }
  .card__bg { position: absolute; inset: 0; }

  /* Contact side */
  .contact { background: var(--grey); }
  .name-tab {
    position: absolute; left: 22px; top: 34px; color: var(--on-navy);
  }
  .name-tab__name {
    font-size: 19px; font-weight: 600; letter-spacing: 1.5px; text-transform: uppercase;
  }
  .name-tab__name span { color: #85cae6; font-weight: 400; }
  .name-tab__title {
    margin-top: 4px; font-size: 11px; font-weight: 400; letter-spacing: 1.2px; text-transform: uppercase;
    color: #c9d3de;
  }
  .info { position: absolute; color: var(--ink); font-size: 12.5px; line-height: 1.55; }
  .info__row { display: flex; align-items: flex-start; gap: 10px; }
  .info__row + .info__row { margin-top: 8px; }
  .info__icon { width: 15px; height: 15px; flex: none; margin-top: 2px; }
  .info--address { left: 22px; top: 132px; }
  .info--reach { left: 312px; top: 206px; }

  .wordmark {
    position: absolute; display: flex; align-items: center; gap: 10px;
    font-weight: 300; text-transform: uppercase; letter-spacing: 4px;
  }
  .wordmark__square { width: 14px; height: 14px; background: currentColor; }
  .contact .wordmark { left: 320px; top: 70px; color: var(--on-navy); font-size: 22px; }

  /* Brand side */
  .brand { background: var(--white); }
  .brand .wordmark { left: 0; right: 0; top: 86px; justify-content: center; color: var(--accent); font-size: 30px; letter-spacing: 6px; }
  .socials {
    position: absolute; left: 0; right: 0; top: 214px;
    display: flex; justify-content: center; gap: 70px;
    color: var(--on-navy); font-size: 12.5px; letter-spacing: .4px;
  }
  .socials__item { display: flex; align-items: center; gap: 8px; }
  .socials__dot { width: 13px; height: 13px; border: 1.5px solid currentColor; border-radius: 50%; }
</style>
</head>
<body>
<main class="stage">

  <section class="card contact" aria-label="Contact side">
    <svg class="card__bg" viewBox="0 0 520 297" aria-hidden="true">
      <polygon points="218,0 520,0 520,182 282,182" fill="#ffffff"/>
      <polygon points="232,0 520,0 520,170 292,170" fill="var(--navy)"/>
      <polygon points="0,22 196,22 222,55 196,88 0,88" fill="var(--navy-tab)"/>
    </svg>

    <div class="name-tab">
      <p class="name-tab__name">Mark <span>Dunn</span></p>
      <p class="name-tab__title">CEO / Technical Director</p>
    </div>

    <div class="info info--address">
      <div class="info__row">
        <svg class="info__icon" viewBox="0 0 16 16" aria-hidden="true"><path d="M8 1.5a4.5 4.5 0 0 0-4.5 4.5c0 3.3 4.5 8.5 4.5 8.5s4.5-5.2 4.5-8.5A4.5 4.5 0 0 0 8 1.5z" fill="none" stroke="var(--ink-soft)" stroke-width="1.3"/><circle cx="8" cy="6" r="1.6" fill="var(--ink-soft)"/></svg>
        <p>Suite 512, 208-3370<br>Harwood Avenue NW</p>
      </div>
    </div>

    <div class="info info--reach">
      <div class="info__row">
        <svg class="info__icon" viewBox="0 0 16 16" aria-hidden="true"><rect x="4" y="1.5" width="8" height="13" rx="1.5" fill="none" stroke="var(--ink-soft)" stroke-width="1.3"/><line x1="7" y1="12" x2="9" y2="12" stroke="var(--ink-soft)" stroke-width="1.3"/></svg>
        <p>(587) 943 - 0586</p>
      </div>
      <div class="info__row">
        <svg class="info__icon" viewBox="0 0 16 16" aria-hidden="true"><rect x="1.5" y="3.5" width="13" height="9" fill="none" stroke="var(--ink-soft)" stroke-width="1.3"/><polyline points="1.5,3.5 8,9 14.5,3.5" fill="none" stroke="var(--ink-soft)" stroke-width="1.3"/></svg>
        <p>mdunn@lumavault.ca</p>
      </div>
    </div>

    <p class="wordmark"><span class="wordmark__square"></span>Lumavault</p>
  </section>

  <section class="card brand" aria-label="Brand side">
    <svg class="card__bg" viewBox="0 0 520 297" aria-hidden="true">
      <rect x="0" y="188" width="520" height="109" fill="var(--navy)"/>
      <rect x="0" y="258" width="520" height="18" fill="var(--blue)"/>
      <polygon points="250,258 270,258 260,248" fill="var(--blue)"/>
    </svg>

    <p class="wordmark"><span class="wordmark__square"></span>Lumavault</p>

    <div class="socials">
      <p class="socials__item"><span class="socials__dot"></span>@LumaVaultHQ</p>
      <p class="socials__item"><span class="socials__dot"></span>@lumavaulthq</p>
    </div>
  </section>

</main>
</body>
</html>
```